Premium Juice and Wine Bottle Label

We require a premium label design for a Burgundy style wine bottle - the design should reflect pure and organic theme, with a reference to New Zealand blueberries. The winning design will look high-end, simple but sophisticated. Our logo is attached, refer :

https://www.rvcellar.co.nz and https://www.halopu.co.nz/wines/details/coming-soon-showcase/2018

for inspiration.

Target Market(s)

High-end retail grocery stores, wine shops, bars.

Requirements
Must have
• Label should leave enough space for barcode and nutrients/ingredients etc. Reference to New Zealand, natural-beverage, be very high-end in design. Refer links in project description for inspiration. Refer to attached logo, which must be used - feel free to change colour in order to obtain the best high-class design.
Nice to have
• N/A.
Should not have
• Cartoons or pictures of berries.

```html
<!DOCTYPE html>
<html lang="en">
<head>
<meta charset="utf-8">
<title>Kestrel Lane – Wine Label</title>
<link rel="stylesheet" href="https://fonts.googleapis.com/css2?family=Jost:wght@400;600&display=swap">
<style>
  :root {
    --navy: #2b2e7a;
    --navy-faint: #46498c;
    --paper: #ffffff;
    --red: #d01f26;
    --ink: #1a1a1a;
    --page: #ffffff;
  }
  html, body {
    margin: 0;
    width: 1200px;
    height: 1000px;
    overflow: hidden;
    background: var(--page);
  }
  .canvas {
    position: relative;
    width: 1200px;
    height: 1000px;
    font-family: "Jost", "Futura", sans-serif;
  }
  .label {
    position: absolute;
    left: 150px;
    top: 50px;
    width: 900px;
    height: 900px;
    box-sizing: border-box;
    border: 3px solid var(--navy);
    border-radius: 3px;
    overflow: hidden;
    background: var(--paper);
  }
  .label__field {
    position: absolute;
    inset: 0;
    width: 100%;
    height: 100%;
  }
  .label__origin {
    position: absolute;
    top: 60px;
    left: 0;
    width: 100%;
    text-align: center;
    color: var(--paper);
    font-size: 18px;
    letter-spacing: 0.02em;
    margin: 0;
    font-weight: 400;
  }
  .label__origin strong { font-weight: 600; }
  .label__backdrop-name {
    position: absolute;
    top: 70px;
    left: 10px;
    margin: 0;
    font-size: 230px;
    line-height: 1;
    font-weight: 600;
    color: var(--navy-faint);
    white-space: nowrap;
    letter-spacing: -0.02em;
  }
  .brand {
    position: absolute;
    top: 330px;
    left: 0;
    width: 100%;
    display: flex;
    justify-content: center;
    align-items: center;
    gap: 18px;
  }
  .brand__mark {
    width: 34px;
    height: 34px;
    background: var(--red);
  }
  .brand__name {
    margin: 0;
    font-size: 72px;
    font-weight: 600;
    color: var(--red);
    line-height: 1;
  }
  .label__info {
    position: absolute;
    top: 686px;
    left: 0;
    width: 100%;
    margin: 0;
    text-align: center;
    color: var(--ink);
    font-size: 22px;
    font-weight: 400;
    letter-spacing: 0.01em;
  }
</style>
</head>
<body>
  <main class="canvas">
    <section class="label" aria-label="Kestrel Lane wine label">
      <svg class="label__field" viewBox="0 0 900 900" preserveAspectRatio="none" aria-hidden="true">
        <path fill="var(--navy)"
          d="M0 0 H900 V412
             C860 416 820 440 800 440
             C720 436 560 420 400 410
             C320 404 240 390 200 380
             C180 330 150 290 60 280
             C35 278 15 282 0 286 Z"/>
      </svg>
      <p class="label__backdrop-name" aria-hidden="true">Kestrel</p>
      <p class="label__origin"><strong>NEW ZEALAND</strong>, NATURAL-BEVERAGE</p>
      <div class="brand">
        <span class="brand__mark" aria-hidden="true"></span>
        <h1 class="brand__name">Kestrel Lane</h1>
      </div>
      <p class="label__info">BARCODE AND NUTRIENTS/INGREDIENTS</p>
    </section>
  </main>
</body>
</html>
```